Invitation card to the opening of BRAVORA FITNESS CLUB

A successful training plan starts with BRAVORA Fitness!
Join us for our grand opening! OPEN HOUSE AND YOU ARE INVITED!
Tuesday 1st of August, 2017
Classes start from 7.30am till 9.30pm.
Explore the most fun, exciting, challenging and effective training system in the region.
Healthy drinks and delicious food will be provided.
We hope to see you there!

www.bravorafitnessclub.example
APP: BRAVORAFITQZN
Tel: 81-42 09 15

Industry/Entity Type

Fitness

Colors

Designer to choose colors to be used in the design.

Requirements
Must have
• Elegant card
Nice to have
• Logo in the background
Should not have
• pictures

```html
<!DOCTYPE html>
<html lang="en">
<head>
<meta charset="utf-8">
<title>BRAVORA Fitness – Grand Opening Invitation</title>
<link href="https://fonts.googleapis.com/css2?family=Cinzel:wght@400&family=Montserrat:wght@300;600&family=Raleway:wght@300;600&family=Great+Vibes&display=swap" rel="stylesheet">
<style>
  :root {
    --ink: #151515;
    --gold: #6b5322;
    --gold-light: #d9c9a4;
    --gold-mid: #b9a57c;
    --silver-light: #eeeeee;
    --silver-mid: #c9c9c9;
    --silver-dark: #9d9d9d;
    --paper: #ffffff;
  }
  html, body {
    margin: 0;
    padding: 0;
    overflow: hidden;
    background: var(--paper);
  }
  .card {
    position: relative;
    width: 1200px;
    height: 857px;
    overflow: hidden;
    background: var(--paper);
    color: var(--ink);
  }
  .backdrop {
    position: absolute;
    inset: 0;
  }
  .centered {
    position: absolute;
    left: 0;
    width: 894px;
    text-align: center;
    margin: 0;
    white-space: nowrap;
  }
  .masthead {
    width: 852px;
  }
  .tagline {
    top: 36px;
    font-family: "Montserrat", sans-serif;
    font-weight: 600;
    font-size: 27px;
    letter-spacing: 3px;
    line-height: 1.1;
  }
  .tagline .lead { font-weight: 300; }
  .brand-name {
    top: 80px;
    font-family: "Cinzel", serif;
    font-weight: 400;
    font-size: 110px;
    letter-spacing: 8px;
    line-height: 1;
  }
  .brand-sub {
    top: 184px;
    font-family: "Cinzel", serif;
    font-weight: 400;
    font-size: 36px;
    letter-spacing: 36px;
    padding-left: 36px;
    line-height: 1;
  }
  .intro {
    top: 252px;
    font-family: "Raleway", sans-serif;
    font-weight: 300;
    font-size: 29px;
    line-height: 1.1;
  }
  .headline {
    top: 292px;
    font-family: "Great Vibes", cursive;
    font-weight: 400;
    font-size: 82px;
    color: var(--gold);
    line-height: 1.1;
  }
  .body-copy {
    font-family: "Raleway", sans-serif;
    font-weight: 300;
    font-size: 27px;
    line-height: 1.3;
  }
  .body-copy strong { font-weight: 600; }
  .invite { top: 417px; }
  .schedule { top: 478px; }
  .explore { top: 586px; }
  .refreshments { top: 679px; }
  .signoff {
    top: 750px;
    font-family: "Great Vibes", cursive;
    font-size: 64px;
    color: var(--gold);
    line-height: 1.1;
  }
  .side-brand {
    position: absolute;
    left: 934px;
    width: 240px;
    top: 110px;
    text-align: center;
    font-family: "Cinzel", serif;
    font-weight: 400;
    color: var(--ink);
  }
  .side-brand .name { display: block; font-size: 48px; line-height: 1; }
  .side-brand .sub { display: block; font-size: 14px; letter-spacing: 12px; padding-left: 12px; margin-top: 6px; }
  .contact {
    position: absolute;
    left: 914px;
    width: 280px;
    top: 206px;
    text-align: center;
    font-family: "Raleway", sans-serif;
    font-weight: 300;
    font-size: 17px;
    line-height: 26px;
    color: var(--ink);
  }
  .contact p { margin: 0; white-space: nowrap; }
  .contact .web { font-weight: 600; }
</style>
</head>
<body>
<main class="card">
  <svg class="backdrop" width="1200" height="857" viewBox="0 0 1200 857">
    <defs>
      <radialGradient id="silverGlow" cx="0.6" cy="0.35" r="0.9">
        <stop offset="0" stop-color="#eeeeee"/>
        <stop offset="0.5" stop-color="#c9c9c9"/>
        <stop offset="1" stop-color="#9d9d9d"/>
      </radialGradient>
      <linearGradient id="goldBand" x1="0" y1="0" x2="0" y2="1">
        <stop offset="0" stop-color="#d9c9a4"/>
        <stop offset="0.6" stop-color="#b9a57c"/>
        <stop offset="1" stop-color="#a08c63"/>
      </linearGradient>
      <filter id="edgeShadow" x="-10%" y="-10%" width="130%" height="120%">
        <feDropShadow dx="4" dy="0" stdDeviation="5" flood-color="#000" flood-opacity="0.25"/>
      </filter>
    </defs>
    <rect class="sparkle-panel" x="0" y="0" width="1200" height="857" fill="url(#silverGlow)" role="img" aria-label="Silver bokeh sparkle background"/>
    <path class="gold-band" d="M850,0 C905,190 965,470 1042,857 L0,857 L0,0 Z" fill="url(#goldBand)"/>
    <path class="band-edge" d="M850,0 C905,190 965,470 1042,857" fill="none" stroke="#ffffff" stroke-width="2"/>
    <path class="paper-panel" d="M812,0 C900,130 952,330 940,500 C930,640 885,760 842,857 L0,857 L0,0 Z" fill="#ffffff" filter="url(#edgeShadow)"/>
  </svg>

  <p class="centered masthead tagline"><span class="lead">A</span> SUCCESSFUL TRAINING PLAN STARTS WITH</p>
  <p class="centered masthead brand-name">BRAVORA</p>
  <p class="centered masthead brand-sub">FITNESS</p>

  <p class="centered intro">Join us for our</p>
  <p class="centered headline">Grand Opening!</p>

  <p class="centered body-copy invite">OPEN HOUSE AND YOU ARE INVITED!</p>
  <p class="centered body-copy schedule">Tuesday 1st of <strong>August, 2017</strong><br>Classes start from <strong>7.30am till 9.30pm.</strong></p>
  <p class="centered body-copy explore">Explore the most fun, exciting, challenging and effective<br>training system in the region.</p>
  <p class="centered body-copy refreshments">Healthy drinks and delicious food will be provided.</p>
  <p class="centered signoff">We hope to see you there!</p>

  <div class="side-brand">
    <span class="name">BRAVORA</span>
    <span class="sub">FITNESS</span>
  </div>
  <div class="contact">
    <p class="web">www.bravorafitnessclub.example</p>
    <p>APP: BRAVORAFITQZN</p>
    <p>TEL: 81-42 09 15</p>
  </div>
</main>
</body>
</html>
```